Beautiful Upgraded Single Story Home in Avonlea...SOLD in 3 days for top $$!

This is a 6.5" x 11" QRVL postcard. Please use the indicia files and 6.5" x 11" template attached in the brief.

Reason: We are still working on the details for one of the postcards. Thanks

Target Market(s)

Listings

Font styles to use
Serif

Colors
33b8a4

Requirements
Must have
• Call me if you are interested in getting the most amount of equity out of your home!
• Marisol Denning (555) 814-3067 and Odile Pranwick (555) 372-9140
• Marisol@GroupPranwick.example and Odile@GroupPranwick.example
• Brightwater Properties
• The Key to your Real Estate Needs!
• (At bottom of postcard) "If you are currently listed with a licensed Realtor, this is not intended as solicitation"
Nice to have
• The Front Should be the Property Picture and "In Escrow in 3 Days!"

```html
<!DOCTYPE html>
<html lang="en">
<head>
<meta charset="utf-8">
<title>Brightwater Properties – In Escrow in 3 Days Postcard</title>
<link rel="stylesheet" href="https://fonts.googleapis.com/css2?family=Lora:wght@400;500&family=Montserrat:wght@400;500&display=swap">
<style>
  :root {
    --teal: #33b8a4;
    --teal-deep: #2aa592;
    --ink: #1d1d1d;
    --paper: #ffffff;
    --backdrop: #e9ecec;
    --sky: #a9c9e6;
    --lawn: #6f9d4a;
    --house: #5b7391;
    --room-warm: #c89664;
    --room-light: #eef0ee;
    --couple-tone: #efe7e0;
  }
  * { box-sizing: border-box; margin: 0; padding: 0; }
  html, body {
    width: 1200px; height: 900px; overflow: hidden;
    background: var(--backdrop);
    font-family: "Montserrat", sans-serif;
    color: var(--ink);
  }
  .stage {
    width: 1200px; height: 900px;
    display: flex; flex-direction: column; align-items: center; justify-content: center;
    gap: 26px;
  }
  .postcard {
    position: relative;
    width: 700px; height: 414px;
    background: var(--paper);
    overflow: hidden;
    box-shadow: 0 6px 18px rgba(0,0,0,.18);
  }

  /* Front */
  .front-edge { position: absolute; left: 0; top: 0; width: 34px; height: 100%; background: var(--teal); }
  .front-edge-foot { position: absolute; left: 0; bottom: 0; width: 300px; height: 18px; background: var(--teal); }
  .property-photo {
    position: absolute; left: 34px; top: 0; width: 266px; height: 396px;
    background: linear-gradient(180deg, var(--sky) 0%, #c7dbee 30%, var(--house) 55%, #7c8fa5 72%, var(--lawn) 82%, #5c8a3a 100%);
  }
  .brand-tag {
    position: absolute; left: 58px; top: 38px;
    padding: 8px 12px; background: var(--paper);
    font-family: "Lora", serif; font-size: 17px; font-weight: 400; color: var(--ink);
    line-height: 1.15;
  }
  .headline {
    position: absolute; left: 330px; top: 38px;
    font-family: "Lora", serif; font-weight: 400;
    font-size: 44px; line-height: 1.05; color: var(--teal);
  }
  .couple-photo {
    position: absolute; left: 420px; top: 150px; width: 280px; height: 264px;
    background: radial-gradient(ellipse at 40% 50%, #d9c3b0 0%, var(--couple-tone) 55%, #f7f5f2 100%);
  }

  /* Back */
  .interior-photo {
    position: absolute; left: 0; top: 0; width: 322px; height: 160px;
    background: linear-gradient(90deg, var(--room-warm) 0%, #dcb48a 30%, var(--room-light) 55%, #f4f5f3 75%, #8fb36a 100%);
  }
  .equity-callout {
    position: absolute; left: 322px; top: 0; width: 248px; height: 132px;
    background: var(--teal);
    color: var(--paper);
    font-size: 16.5px; font-weight: 500; line-height: 1.3;
    padding: 22px 20px;
  }
  .indicia-box {
    position: absolute; right: 28px; top: 26px; width: 72px; height: 72px;
    border: 1.5px solid #555;
  }
  .back-brand {
    position: absolute; left: 462px; top: 160px;
    font-family: "Lora", serif; font-size: 17px; color: var(--ink);
  }
  .contacts {
    position: absolute; left: 34px; top: 186px;
    font-size: 14.5px; line-height: 1.35;
  }
  .contacts .name, .contacts .tagline { color: var(--teal); }
  .contacts .block { margin-bottom: 12px; }
  .disclaimer {
    position: absolute; left: 0; bottom: 0; width: 100%; height: 38px;
    background: var(--teal); color: var(--paper);
    font-size: 12.5px; font-style: italic;
    display: flex; align-items: center; padding-left: 34px;
  }
</style>
</head>
<body>
<main class="stage">
  <section class="postcard postcard-front" aria-label="Postcard front">
    <div class="front-edge"></div>
    <div class="property-photo" role="img" aria-label="Photo of a two-story blue-gray house with a green lawn under a blue sky"></div>
    <div class="front-edge-foot"></div>
    <div class="brand-tag">Brightwater<br>Properties</div>
    <h1 class="headline">In Escrow<br>in 3 Days!</h1>
    <div class="couple-photo" role="img" aria-label="Photo of a couple lying on the floor reviewing house plans"></div>
  </section>

  <section class="postcard postcard-back" aria-label="Postcard back">
    <div class="interior-photo" role="img" aria-label="Photo of a modern home interior opening onto a garden"></div>
    <p class="equity-callout">Call me if you are interested in getting the most amount of equity out of your home!</p>
    <div class="indicia-box" aria-label="Postage indicia area"></div>
    <div class="back-brand">Brightwater Properties</div>
    <div class="contacts">
      <div class="block">
        <div><span class="name">Marisol Denning</span> (555) 814-3067</div>
        <div><span class="name">Odile Pranwick</span> (555) 372-9140</div>
      </div>
      <div class="block">
        <div>Marisol@GroupPranwick.example</div>
        <div>Odile@GroupPranwick.example</div>
      </div>
      <div class="block">
        <div>Brightwater Properties</div>
        <div class="tagline">The Key to your Real Estate Needs!</div>
      </div>
    </div>
    <p class="disclaimer">"If you are currently listed with a licensed Realtor, this is not intended as solicitation"</p>
  </section>
</main>
</body>
</html>
```